New Website for Asia Travel Agency

Lanternpath Journeys Website

We want a redesign for our current website, www.lanternpathjourneys.example. We want you to get creative with our brand and present our company in a unique, creative and compelling way, that communicates our exotic destinations and tours, the local and authentic character of our travel consultants and the trustworthy and professional nature of our company.

Who is this company?

Lanternpath Journeys is an online tour operator specializing in providing tailor-made tours to eight destinations in Asia; Vietnam, Thailand, Laos, Cambodia, Indonesia, Myanmar, Japan and China. They were launched in mid February 2012 with headquarters in Bangkok, Thailand, and staffed by locals and expats with many years of experience in the travel industry, and who are committed to sharing their deep knowledge of, and passion for the region.

Local knowledge

Our consultants at Lanternpath Journeys are all locals – they know their destinations inside-out and draw upon invaluable first-hand experience and information when planning your tour. They have insights into local culture and tradition, they know the best places to visit, the most worthwhile experiences to have and, most importantly, they have the knowledge to create exactly the holiday you desire.

All hotels and activities featured in a Lanternpath Journeys tour are regularly inspected by our consultants to ensure the highest quality standards are met and that all information is correct and up to date.

Unforgettable Travel Experiences

Whether it's a cultural exploration or a beach holiday you're after – or a mix of both – Lanternpath Journeys has an itinerary for you – and if we don't have one, we'll tailor-make one! From the main sights to remote villages, our locally based Travel Specialists will give you unique insights into every place you visit and let you delve into known destinations from new perspectives.

Our tours offer a variety of hotel and resort options, premium stays in deluxe accommodation, heritage hotels, a five-star boutique or on the water in a junk. Tap into our experience let us create an experience unique to you – and one you will never forget.

What type of Holiday to Asia?

Our itineraries at Lanternpath Journeys are created according to different inspirations. Some travelers are interested in the History & Culture of a destination, while some like to stay active with Adventure tours. A Cross Border trip explores different countries in a single tour, while Velvet Summit tours offer the highest level of exclusivity across our destinations. There are 14 different Holiday Types to choose from, or you can mix and match ideas to create your dream vacation.

Target Market(s)

Slightly more female, aged 30-65, are creative, professional and looking for something different, something a bit unusual.

Industry/Entity Type

Boutique

Requirements
Must have
• 5 page designs:

1. Homepage
2. Tours list page for a country
3. Tour page
4. 'Be Inspired' page
5. Country page
6. Enquiry page

Our inspirations.

The following list shows websites we love and which inspire us... to give you some indication of our preferred styles, functions and layouts:

http://www.frostmeridian.example/en/ (we really like this, great personality, like the use of icons for tour types)
http://www.pebblewalks.example.uk/ (very simple design elements and layout)
http://www.sunvalecoast.example/ (great use of background image, nice simple nav bar)
http://www.roamcedarfall.example/ (we like because it has distinct personality and is well suited to the destination)
http://www.seemarlowton.example/ (clear personality through font use)
http://www.vastroving.example/ (original, unique)
http://www.wanderquill.example/long-loop-of-asia (like the map style)

Key design points:

1. You must use our existing logo (attached), but you can change the color scheme of the logo to accord with the whichever color scheme you choose for the main designs.
2. Our logo strapline is "Asia is our Lanternpath" and should be used prominently on the page to reinforce the meaning of our company name.
3. Home page and tours list pages should allow the user to see the choice of tours immediately without scrolling & Introduction copy should be minimal.
4. We and our site visitors are inspired and excited by our photography, this is an element of the site which we would like to maintain and build on, though the section page header sliders are currently too big and do not allow quick access to the section content. This is a design problem which needs a solution. Full page photographic backgrounds may be an answer?
5. Tour page should display other contextual tours, from the same country or style/type
6. We should promote press coverage in various places
7. We should display consultant profiles in various places
8. Map designs for tour page and country page, plus a modal pop out for the home page. These are complex and may have a few small photos and short descriptive text only, though this is limited by your own creativity. We will use graphics and html5/css3 so there are no creative limitations.
9. The 'Inspirations' / 'Be Inspired' page is for people who want travel and holiday ideas, who are looking for inspiration on where to go and what to do. This section needs to reflect the exotic, the unusual, the extraordinary in our destinations and tours, and we leave this to your creative genius to develop. We are also interested in how this inspirations page is related to the blog and social media content we produce daily, is there an integration here? Can we present YouTube videos, our blog posts, Facebook posts etc, on this page? This is another design challenge.
10. We would like to see designs for the tours list page which feature AJAX content filtering (for instance: http://demo.layoutbrisk.example/?acn), we would like to see how to include this type of content filtering on homepage and destination page also.
11. The 'Enquiry' call to action should be on all pages and prominent.
12. The enquiry page can reflect the same fields as the existing website enquiry page

Values to be communicated:

- Exotic: Asia is exotic, and our tours will expose clients to extraordinary sights and unusual cultural encounters.
- Authentic: Our travel consultants all live in the destinations themselves, they are local nationals and have all the insider knowledge to give clients a truly authentic experience of our destinations
- Unique: All of our tours are tailor made, there are no fixed departure dates or join-in groups. All tour itineraries can be uniquely designed for our clients, from departure dates to destinations.
- Trust: Some travelers prefer to book their holidays with local agencies they can meet in person, rather than with online companies like us who live in the destinations and who they only get to meet on Skype video or phone. We want to convey that we are trustworthy. We have attempted this through presenting a 'meet the team' page and a 'press' page and advert, as well as offering a prominent international phone number. How we you build on this and further convey this value?

```html
<!DOCTYPE html>
<html lang="en">
<head>
<meta charset="utf-8">
<title>Lanternpath Journeys — Home</title>
<link href="https://fonts.googleapis.com/css2?family=Lato:wght@400;700;900&display=swap" rel="stylesheet">
<style>
:root{
  --teal:#2aa39a;
  --teal-dark:#1f8a82;
  --orange:#f08a24;
  --ink:#222;
  --text:#555;
  --muted:#888;
  --line:#ddd;
  --footer:#3b3b3b;
  --footer-text:#bdbdbd;
  --bar:#f1f1f1;
  --white:#fff;
}
*{box-sizing:border-box;margin:0;padding:0}
html,body{width:692px;height:1200px;overflow:hidden;background:var(--white)}
body{font-family:'Lato',Arial,sans-serif;color:var(--text);position:relative}
.abs{position:absolute}

/* header */
.site-header{left:0;top:0;width:692px;height:40px;background:var(--white);border-bottom:1px solid var(--line)}
.brand{left:14px;top:11px;display:flex;align-items:center;gap:6px;font-size:13px;font-weight:700;color:var(--teal)}
.brand-mark{width:16px;height:16px;background:var(--teal);border-radius:2px}
.main-nav{left:200px;top:10px;display:flex;gap:4px;font-size:9px;font-weight:700;color:#444}
.main-nav span{padding:5px 7px}
.main-nav .active{color:var(--teal);border:1px solid var(--line);background:#f6f6f6}
.header-search{left:578px;top:11px;width:100px;height:18px;background:var(--teal);border-radius:2px}
.header-search svg{position:absolute;right:5px;top:4px}

/* hero */
.hero{left:0;top:40px;width:692px;height:370px;background:linear-gradient(180deg,#e8ece8 0%,#cfd8cf 45%,#8a9a85 100%)}
.hero-title{left:14px;top:62px;font-size:44px;font-weight:900;color:var(--ink);letter-spacing:-1px}
.promo{left:12px;top:150px;width:478px;height:230px;background:rgba(28,34,28,.78)}
.promo-label{left:10px;top:8px;font-size:10px;font-weight:700;color:var(--white);letter-spacing:.5px}
.promo-photo{left:10px;top:28px;width:226px;height:192px;background:linear-gradient(160deg,#7fb24a,#3f7a2a 60%,#2d5a22)}
.promo-body{left:250px;top:34px;width:215px;color:var(--white)}
.promo-body h2{font-size:19px;font-weight:700;letter-spacing:.3px}
.promo-body .nights{font-size:9px;margin-top:3px;letter-spacing:.5px}
.promo-body .price{font-size:24px;font-weight:900;margin-top:12px}
.promo-body .price small{font-size:10px;font-weight:400}
.promo-body p{font-size:9px;line-height:1.45;margin-top:12px;color:#e4e4e4}
.btn{display:inline-block;background:var(--orange);color:var(--white);font-size:9px;font-weight:700;padding:6px 10px;border-radius:2px}
.promo-body .btn{margin-top:14px}

.search-panel{left:504px;top:150px;width:176px;height:230px;background:var(--teal);padding:8px 10px}
.search-panel h3{font-size:10px;font-weight:900;color:var(--white);letter-spacing:.4px;margin-bottom:8px}
.field-label{font-size:7px;font-weight:700;color:var(--white);margin-top:5px}
.select{height:15px;background:var(--white);font-size:7px;color:#555;padding:3px 5px;margin-top:2px;position:relative}
.select::after{content:"";position:absolute;right:5px;top:6px;border:3px solid transparent;border-top-color:#777}
.search-panel .btn{display:block;text-align:center;margin-top:12px;font-size:10px}

.hero-dots{left:318px;top:392px;display:flex;gap:6px}
.dot{width:7px;height:7px;border-radius:50%;background:#bbb}
.dot.on{background:var(--orange)}

/* why + press */
.why{left:14px;top:425px;width:328px;height:84px;border:1px solid var(--line);padding:10px 14px}
.why h3{font-size:17px;font-weight:400;color:#666}
.why p{font-size:8px;line-height:1.45;margin-top:6px;color:var(--muted)}
.why a{font-size:8px;color:var(--teal);text-decoration:none;display:block;margin-top:4px}
.press{left:350px;top:425px;width:328px;height:84px;border:2px solid var(--teal);padding:8px 14px}
.press h3{font-size:17px;font-weight:400;color:var(--teal)}
.press .meta{font-size:8px;color:var(--muted);margin-top:4px;line-height:1.4}
.press .meta b{color:#444}
.press .btn{background:var(--teal);margin-top:6px;font-size:8px;padding:4px 8px}

/* hot destinations */
.blossom{left:0;top:530px;width:260px;height:180px;background:radial-gradient(ellipse at 30% 40%,rgba(230,150,170,.35),rgba(255,255,255,0) 70%)}
.section-label{left:14px;top:552px;font-size:9px;font-weight:900;color:#333;letter-spacing:.3px}
.slider-dots{left:648px;top:553px;display:flex;gap:4px}
.slider-dots .dot{width:6px;height:6px}
.dest{top:568px;width:205px;height:106px}
.dest .cap{position:absolute;left:10px;bottom:9px;color:var(--white);font-weight:700;font-size:10px;line-height:1.2;width:150px}
.dest .cap.big{font-size:20px}
.dest .plus{position:absolute;right:9px;bottom:6px;color:var(--white);font-size:20px;font-weight:700}
.dest-1{left:46px;background:linear-gradient(180deg,#6aa7c9,#c8432e 55%,#4a6a3a)}
.dest-2{left:259px;background:linear-gradient(180deg,#9aa3a8,#4f5b52 60%,#2e3a30)}
.dest-3{left:472px;background:linear-gradient(135deg,#d9492c,#e7a12d 45%,#9e2a1d)}

/* testimonials */
.quote{top:690px;width:205px}
.quote h4{font-size:10px;font-weight:900;color:#333}
.quote p{font-size:8px;line-height:1.45;color:var(--muted);margin-top:3px}
.quote .who{font-size:6.5px;color:var(--orange);font-weight:700;margin-top:4px;letter-spacing:.3px}
.q1{left:14px}.q2{left:240px}.q3{left:466px}

/* skyline + footer */
.skyline{left:0;top:785px;width:692px;height:132px;background:linear-gradient(180deg,rgba(59,59,59,0) 0%,rgba(59,59,59,.35) 45%,var(--footer) 100%)}
.site-footer{left:0;top:917px;width:692px;height:248px;background:var(--footer)}
.f-col{top:18px}
.f-col h5{font-size:8px;font-weight:900;color:var(--white);letter-spacing:.4px;margin-bottom:6px}
.f-col li{list-style:none;font-size:7.5px;color:var(--footer-text);line-height:1.6}
.fc1{left:14px}.fc2{left:110px}.fc3{left:200px}
.fc4{left:360px;width:300px}
.fc4 p{font-size:7.5px;color:var(--footer-text);line-height:1.5}
.sub-row{display:flex;gap:6px;margin-top:8px}
.sub-input{width:190px;height:17px;background:var(--white);border-radius:2px}
.sub-row .btn{font-size:8px;padding:4px 10px}
.follow{left:460px;top:145px;text-align:center}
.follow h5{font-size:8px;font-weight:900;color:var(--white);letter-spacing:.4px}
.social{display:flex;gap:6px;margin-top:7px}
.social span{width:15px;height:15px;border-radius:50%;background:#6d6d6d}
.bottom-bar{left:0;top:1165px;width:692px;height:35px;background:var(--bar);font-size:7.5px;color:var(--muted)}
.bottom-bar .l{position:absolute;left:14px;top:14px}
.bottom-bar .r{position:absolute;left:240px;top:14px}
</style>
</head>
<body>

<header class="site-header abs">
  <div class="brand abs"><span class="brand-mark"></span>Lanternpath Journeys</div>
  <nav class="main-nav abs">
    <span class="active">HOME</span>
    <span>TOURS ▾</span>
    <span>HOLIDAY TYPES ▾</span>
    <span>BE INSPIRED</span>
    <span>ABOUT US</span>
  </nav>
  <div class="header-search abs">
    <svg width="10" height="10" viewBox="0 0 10 10"><circle cx="4" cy="4" r="3" fill="none" stroke="#fff" stroke-width="1.3"/><line x1="6.2" y1="6.2" x2="9" y2="9" stroke="#fff" stroke-width="1.3"/></svg>
  </div>
</header>

<section class="hero abs" role="img" aria-label="Background photo of a pagoda among trees under a pale sky"></section>
<h1 class="hero-title abs">Asia is our lanternpath.</h1>

<section class="promo abs">
  <div class="promo-label abs">FEATURED PROMOTIONS</div>
  <div class="promo-photo abs" role="img" aria-label="Photo of green rice terraces in Java"></div>
  <div class="promo-body abs">
    <h2>A JAVANESE JOURNEY</h2>
    <div class="nights">7 DAYS / 6 NIGHTS</div>
    <div class="price">$1153 <small>/person</small></div>
    <p>Java is a cultural enigma and this tour takes you through the heart of the island.</p>
    <span class="btn">Send an enquiry</span>
  </div>
</section>

<aside class="search-panel abs">
  <h3>SEARCH FOR MORE</h3>
  <div class="field-label">COUNTRY</div><div class="select">ALL COUNTRIES</div>
  <div class="field-label">CITY</div><div class="select">ALL CITIES</div>
  <div class="field-label">DURATION</div><div class="select">ALL DURATIONS</div>
  <div class="field-label">HOLIDAY TYPE</div><div class="select">ALL HOLIDAY TYPES</div>
  <span class="btn">SEARCH</span>
</aside>

<div class="hero-dots abs"><span class="dot on"></span><span class="dot"></span><span class="dot"></span></div>

<section class="why abs">
  <h3>Why Lanternpath Journeys?</h3>
  <p>No one knows a destination better than someone who lives, works and plays there. That's the foundation of Lanternpath Journeys.</p>
  <a>Click here to find out more about us »</a>
</section>

<section class="press abs">
  <h3>Read our latest press coverage</h3>
  <div class="meta"><b>Globe Wire Edition - 28 July 2012</b><br>Quiet Cambodia: a slower journey through temples and villages</div>
  <span class="btn">Find out more</span>
</section>

<div class="blossom abs" role="img" aria-label="Faint cherry blossom branch decoration"></div>
<div class="section-label abs">HOT DESTINATIONS</div>
<div class="slider-dots abs"><span class="dot on"></span><span class="dot"></span></div>

<article class="dest dest-1 abs" role="img" aria-label="Photo of a red shrine gate by a lake">
  <div class="cap">Mt. Fuji's Gate:<br>Discover beautiful Hakone</div><span class="plus">+</span>
</article>
<article class="dest dest-2 abs" role="img" aria-label="Photo of the Great Wall across misty hills">
  <div class="cap big">Epic China</div><span class="plus">+</span>
</article>
<article class="dest dest-3 abs" role="img" aria-label="Photo of colourful lanterns at a night market">
  <div class="cap">Honeymoon in Thailand<br>&amp; Velvet Summit Honeymoon</div><span class="plus">+</span>
</article>

<section class="quote q1 abs">
  <h4>GREAT SUCCESS</h4>
  <p>It was a terrific trip and we are most grateful for the careful attention you gave to all our requests.</p>
  <div class="who">MR. OREN CALDWELL, UK FAMILY</div>
</section>
<section class="quote q2 abs">
  <h4>AN ITINERARY JUST RIGHT</h4>
  <p>We had a great trip. Thank you so much for all the preparation work to get the itinerary just right.</p>
  <div class="who">ILSE VARNDT, GERMANY</div>
</section>
<section class="quote q3 abs">
  <h4>AMAZING JOURNEY,<br>THANKS SO MUCH</h4>
  <p>Back now and still recovering from our amazing journey. It was a fantastic trip.</p>
  <div class="who">MRS. TAMSIN ROWE, AUSTRALIA</div>
</section>

<div class="skyline abs" role="img" aria-label="Silhouette of Asian temples and pagodas along the skyline"></div>

<footer class="site-footer abs">
  <div class="f-col fc1 abs"><h5>QUICK LINKS</h5><ul><li>Home</li><li>Destinations</li><li>Tours</li><li>Holiday Types</li><li>Best Value</li><li>About Us</li><li>Blog</li></ul></div>
  <div class="f-col fc2 abs"><h5>OUR LANTERNPATH</h5><ul><li>Thailand</li><li>Indonesia</li><li>Laos</li><li>Cambodia</li><li>Japan</li><li>Myanmar</li><li>Vietnam</li><li>China</li><li>Multi-Country</li></ul></div>
  <div class="f-col fc3 abs"><h5>ABOUT US</h5><ul><li>Why Book With Us</li><li>About Us</li><li>Meet The Team</li><li>Careers</li><li>In The Press</li><li>Affiliate Program</li></ul></div>
  <div class="f-col fc4 abs">
    <h5>SUBSCRIBE TO OUR E-NEWSLETTER</h5>
    <p>Sign up for Lanternpath Journeys e-newsletter featuring promotions, travel inspiration and insider destinations.</p>
    <div class="sub-row"><span class="sub-input"></span><span class="btn">SUBSCRIBE</span></div>
  </div>
  <div class="follow abs">
    <h5>FOLLOW US</h5>
    <div class="social"><span></span><span></span><span></span><span></span></div>
  </div>
</footer>

<div class="bottom-bar abs">
  <span class="l">Contact Us | Terms</span>
  <span class="r">© 2013 Lanternpath Journeys All Rights Reserved</span>
</div>

</body>
</html>
```